Velmora Grove Club Postcard Design

Need a postcard for this business. Go to velmoragroveclub.com to see the product we are selling. Here's another good postcard you can sample. https://www.rowanpilsbydesign.com/?lightbox=dataItem-qz4tunal
Another one: http://blog.tranquet.com/postcard-examples-from-popular-startups/

```html
<!DOCTYPE html>
<html lang="en">
<head>
<meta charset="utf-8">
<title>Velmora Grove Club Postcard</title>
<link rel="stylesheet" href="https://fonts.googleapis.com/css2?family=Alegreya:wght@400;500;700&family=Kaushan+Script&display=swap">
<style>
  :root {
    --page: #ececec;
    --sage: #b4c99f;
    --sage-deep: #9fb78a;
    --lime: #8cc34b;
    --ink: #333333;
    --banner: #3a3a3a;
    --clay: #c0725f;
    --clay-dark: #8e4a3c;
    --paper: #f4f4f4;
    --white: #ffffff;
    --photo-dog-a: #8a6b4a;
    --photo-dog-b: #d9b47c;
    --photo-stick: #b5733a;
    --icon-dark: #2b2b2b;
    --icon-box: #c9a46a;
  }
  * { box-sizing: border-box; margin: 0; padding: 0; }
  html, body { width: 1200px; height: 800px; overflow: hidden; }
  body { background: var(--page); font-family: "Alegreya", Georgia, serif; color: var(--ink); position: relative; }

  .postcard { position: absolute; top: 205px; width: 570px; height: 390px; overflow: hidden; box-shadow: 0 6px 18px rgba(0,0,0,.18); }
  .postcard--front { left: 20px; background: var(--paper); }
  .postcard--back { left: 610px; background: var(--white); }

  .abs { position: absolute; }

  /* front */
  .hero { left: 0; top: 0; width: 570px; height: 228px; background: var(--sage); }
  .hero-rule { left: 0; top: 226px; width: 570px; height: 3px; background: var(--lime); }
  .photo { border-radius: 6px; }
  .photo--dog-left { left: 38px; top: 50px; width: 112px; height: 175px; background: linear-gradient(180deg, var(--photo-dog-a), #b48d5e); }
  .photo--dog-right { left: 435px; top: 22px; width: 125px; height: 190px; background: linear-gradient(180deg, var(--photo-dog-b), #c99a5c); }

  .offer { left: 160px; width: 270px; text-align: center; }
  .offer-lead { top: 16px; font-size: 17px; }
  .offer-headline { top: 38px; font-family: "Kaushan Script", cursive; font-size: 50px; line-height: 1.1; color: var(--ink); }
  .offer-sub { top: 104px; font-size: 18px; }
  .join-banner { left: 165px; top: 136px; width: 260px; height: 44px; }
  .join-text { left: 165px; top: 138px; width: 260px; text-align: center; font-family: "Kaushan Script", cursive; font-size: 28px; color: var(--white); }
  .code-line { left: 150px; top: 190px; width: 290px; text-align: center; font-size: 13px; font-weight: 500; }
  .code-pill { display: inline-block; background: var(--clay); color: var(--white); border: 1.5px solid var(--clay-dark); border-radius: 6px; padding: 1px 5px; font-size: 16px; margin: 0 2px; }

  .steps-title { left: 90px; top: 236px; width: 260px; text-align: center; font-size: 25px; font-weight: 500; }
  .steps-title::before, .steps-title::after { content: ""; position: absolute; top: 18px; width: 45px; height: 2px; background: var(--ink); }
  .steps-title::before { left: 0; }
  .steps-title::after { right: 0; }

  .steps-band { left: 0; top: 332px; width: 570px; height: 58px; background: var(--lime); }
  .step-divider { top: 280px; width: 0; height: 106px; border-left: 2px dotted var(--lime); }
  .step-icon { top: 282px; border-radius: 4px; }
  .step-icon--pup { left: 60px; width: 70px; height: 46px; background: linear-gradient(135deg, #e9e2da, #b7826a); }
  .step-icon--cattle { left: 190px; width: 80px; height: 46px; background: var(--icon-dark); }
  .step-icon--parcel { left: 315px; width: 60px; height: 46px; background: var(--icon-box); }
  .step-label { top: 338px; color: var(--white); font-size: 13px; text-align: center; line-height: 1.2; }

  .club-badge { left: 442px; top: 238px; width: 112px; height: 112px; border-radius: 50%; background: var(--white); border: 3px solid var(--ink); display: flex; align-items: center; justify-content: center; text-align: center; font-size: 15px; font-weight: 700; color: var(--ink); line-height: 1.15; padding: 10px; }

  /* back */
  .back-panel { left: 0; top: 0; width: 400px; height: 390px; background: var(--sage); }
  .photo--sticks { left: 22px; top: 16px; width: 356px; height: 130px; background: linear-gradient(160deg, #d6c7a6 0%, var(--photo-stick) 50%, #d6c7a6 100%); }
  .claim-band { left: 20px; top: 152px; width: 370px; height: 50px; background: var(--clay); border-radius: 4px; color: var(--white); font-size: 16.5px; font-weight: 500; line-height: 1.3; padding: 3px 14px; }
  .claim-body { left: 24px; top: 206px; width: 360px; font-size: 10.5px; line-height: 1.55; text-align: justify; }
  .back-rule { left: 0; top: 318px; width: 400px; height: 3px; background: var(--lime); }
  .visit-band { left: 0; top: 324px; width: 400px; height: 66px; background: var(--lime); text-align: center; font-size: 15px; font-weight: 500; padding-top: 18px; }
  .stamp-box { left: 465px; top: 40px; width: 72px; height: 72px; border: 1.5px solid var(--ink); }
  .address-line { left: 420px; width: 135px; height: 0; border-top: 1.5px solid var(--ink); }
</style>
</head>
<body>

<section class="postcard postcard--front" aria-label="Postcard front">
  <div class="abs hero"></div>
  <div class="abs hero-rule"></div>
  <div class="abs photo photo--dog-left" role="img" aria-label="Photo of a small terrier wearing sunglasses"></div>
  <div class="abs photo photo--dog-right" role="img" aria-label="Photo of a golden retriever puppy in a bandana"></div>

  <p class="abs offer offer-lead">Sign up for a subscription &amp;</p>
  <h1 class="abs offer offer-headline">SAVE 50%</h1>
  <p class="abs offer offer-sub">on your first month</p>

  <svg class="abs join-banner" viewBox="0 0 260 44" aria-hidden="true">
    <polygon points="0,4 260,0 250,22 260,44 6,40 14,22" fill="var(--banner)"/>
  </svg>
  <p class="abs join-text">Join The Club</p>

  <p class="abs code-line">Use Code <span class="code-pill">VELMORAGROVE</span> At Checkout</p>

  <h2 class="abs steps-title">How It Works</h2>

  <div class="abs steps-band"></div>
  <div class="abs step-divider" style="left:170px"></div>
  <div class="abs step-divider" style="left:290px"></div>

  <div class="abs step-icon step-icon--pup" role="img" aria-label="Illustration of a happy cartoon puppy with a guarantee seal"></div>
  <div class="abs step-icon step-icon--cattle" role="img" aria-label="Silhouette of a cow marked premium quality"></div>
  <div class="abs step-icon step-icon--parcel" role="img" aria-label="Illustration of a cardboard shipping box"></div>

  <p class="abs step-label" style="left:15px;width:150px;top:344px">Doggy joy guarantee</p>
  <p class="abs step-label" style="left:175px;width:110px">Sourced from free range cattle</p>
  <p class="abs step-label" style="left:295px;width:140px;top:344px">Shipped to your doorstep</p>

  <div class="abs club-badge">Velmora Grove Club</div>
</section>

<section class="postcard postcard--back" aria-label="Postcard back">
  <div class="abs back-panel"></div>
  <div class="abs photo photo--sticks" role="img" aria-label="Photo of three crossed bully sticks"></div>
  <p class="abs claim-band">Velmora Grove provides high-quality, all-natural bully sticks.</p>
  <p class="abs claim-body">Our bully sticks and other products are sourced from grass fed, free range cattle; raised without any added hormones or antibiotics, resulting in a healthier and better tasting treat. Processed in a USDA Human Grade Certified and Inspected facility. Each bully stick is six inches and 8-14 gm each; they're handpicked and inspected to ensure quality, texture and perfect consistency.</p>
  <div class="abs back-rule"></div>
  <p class="abs visit-band">Visit us at: velmoragroveclub.com</p>

  <div class="abs stamp-box" aria-label="Stamp area"></div>
  <div class="abs address-line" style="top:178px"></div>
  <div class="abs address-line" style="top:208px"></div>
  <div class="abs address-line" style="top:238px"></div>
  <div class="abs address-line" style="top:268px"></div>
  <div class="abs address-line" style="top:298px"></div>
</section>

</body>
</html>
```